依頼詳細
PCとスマホデザインの両方納品をいただきますが、
まずはデザインイメージが確認しやすいPCページのみの提案をお願いします。
スマホページは当選者に納品時にお願いしたいと思います。
スマホサイズについて、カンバスサイズは横幅375pxで作成し、2倍の横幅750pxのサイズで書き出ししてください。
(Retinaディスプレイに対応するため)
スマホページ作成時は、メニューが展開した際のデザインもお願いします。
レスポンシブウェブデザインを意識したデザインでお願いします。

■サイトマップ
添付の画面遷移図をご確認ください。

■参考サイト
https://harbor-mend-crew.com/
https://www.qv-tm.co.jp/

■内容について
工場や倉庫の修繕・改修・増築などを専門とするサービスサイトになります。

■素材写真
画像データについては、フリー素材から流用して
イメージ画像に当て込んでください。
足りない場合は、一旦他のサイトの写真をサンプルとして
入れてください。(サンプルなどの表記をお願いします)
また、購入が必要な写真などを利用した場合、
価格とサイト名を教えてください。

また、Nimbrel Stockで定期契約をしていますので、
Nimbrel Stockの画像は使用できます。
デザイン時はカンプ画像をお入れいただきますようお願いします。

■ロゴについて
添付のロゴデータを使用してください。

■ワイヤーフレーム
https://mk.velquora.com/view/600e5e1a-e3bd-4b32-a74b-244a4501d661-355d/?fullscreen
コンテンツの構成としてワイヤーフレームを作成しましたが
必ずしもワイヤーフレームの通りではなくて大丈夫です。
TOPページに配置するコンテンツを見ていただき、デザインは
デザイナーの皆様におまかせしたいと思います。

----------------------------------------------------------------------------
【制作物に対するお願い】

■フォントについて
・無料で使えるフォントで作成をお願いします。
・OSに紐づくフォントの使用は控えていただければと思います (ヒラギノなど)

サイトURL
ページ数
1ページ
希望イメージ
シンプル 複雑
単色 カラフル
暗い 明るい
日常 高級
遊び心 厳粛
未来的 伝統的
女性的 男性的
希望する色
ベースカラー:白、ポイントカラー:赤、青(救急のイメージ)
納品ファイル
• 高解像度JPG (.jpg)
• イラストレーター形式 (.ai)
• フォトショップ形式 (.psd)
補足説明
上記のいずれか1つ(アウトラインありとなしの2つ)と高解像度JPGを納品お願いします。
adobe XDでの納品も可能です。

```html
<!DOCTYPE html>
<html lang="ja">
<head>
<meta charset="utf-8">
<title>ファクトリーケア | 工場専門修繕サービス</title>
<link rel="stylesheet" href="https://fonts.googleapis.com/css2?family=Noto+Sans+JP:wght@400;500;700;900&family=Montserrat:wght@500;700&display=swap">
<style>
:root{
  --blue:#1763c2;
  --blue-dark:#0f4f9e;
  --red:#e2342b;
  --ink:#1f2a37;
  --muted:#7b8591;
  --line:#dfe3e8;
  --paper:#ffffff;
  --mist:#f2f4f6;
  --photo-a:#9fb3c6;
  --photo-b:#5d7286;
}
*{box-sizing:border-box;margin:0;padding:0}
html,body{width:1200px;height:4684px;overflow:hidden}
body{font-family:"Noto Sans JP",sans-serif;color:var(--ink);background:var(--paper);position:relative}
.abs{position:absolute}
.photo{background:linear-gradient(135deg,var(--photo-a),var(--photo-b))}
.en{font-family:"Montserrat",sans-serif;letter-spacing:.12em}

/* header */
.site-header{position:absolute;top:0;left:0;width:1200px;height:96px;background:var(--paper);z-index:3}
.brand{position:absolute;left:30px;top:24px;display:flex;align-items:center;gap:10px}
.brand-mark{width:34px;height:34px;border-radius:50%;background:var(--red)}
.brand-name{font-size:24px;font-weight:900;color:var(--blue)}
.util{position:absolute;right:40px;top:12px;display:flex;align-items:center;gap:20px;font-size:11px;color:var(--muted)}
.util .tel{font-family:"Montserrat",sans-serif;color:var(--red);font-weight:700;font-size:18px}
.util .btn{border:1px solid var(--blue);color:var(--blue);border-radius:14px;padding:4px 14px}
.util .btn.red{border-color:var(--red);color:var(--red)}
.gnav{position:absolute;right:40px;top:58px;display:flex;gap:34px;font-size:13px;font-weight:500}
.gnav .current{color:var(--red);border-bottom:2px solid var(--red);padding-bottom:6px}

/* hero */
.hero{left:0;top:96px;width:1200px;height:524px;border-radius:0 0 0 60px}
.hero-copy{right:120px;top:220px;text-align:left;color:#fff;font-weight:900}
.hero-copy .lead{font-size:40px;letter-spacing:.04em}
.hero-copy .lead em{font-style:normal;color:var(--red)}
.hero-copy .main{font-size:64px;letter-spacing:.04em;margin-top:4px}

/* service intro */
.intro-band{left:0;top:680px;width:1200px;height:640px;background:var(--mist)}
.intro-title{left:260px;top:740px;font-size:34px;font-weight:900;color:var(--blue);line-height:1.4}
.intro-photo{left:0;top:860px;width:220px;height:300px;border-radius:0 40px 40px 0}
.intro-text{left:590px;top:720px;width:440px;font-size:13px;line-height:2.3;color:var(--ink)}
.pill{display:inline-flex;align-items:center;gap:10px;border:1px solid var(--red);color:var(--red);border-radius:20px;padding:8px 22px;font-size:13px;font-weight:500;background:#fff}
.pill::after{content:"";width:6px;height:6px;border-radius:50%;background:var(--red)}
.pill.white{border-color:#fff;color:#fff;background:transparent}
.pill.white::after{background:#fff}
.intro-btn{left:600px;top:980px}
.intro-photo2{left:860px;top:1010px;width:340px;height:250px;border-radius:40px 0 0 40px}
.intro-bg-word{left:-10px;top:1240px;font-family:"Montserrat",sans-serif;font-size:110px;font-weight:700;color:transparent;-webkit-text-stroke:1px #d5dae0;white-space:nowrap}

/* works */
.sec-title{font-size:30px;font-weight:900;color:var(--blue)}
.works-title{left:160px;top:1380px}
.works-btn{left:880px;top:1376px}
.works-band{left:0;top:1540px;width:1200px;height:930px;background:var(--blue)}
.work-card{top:1500px;width:300px;height:310px;background:#fff;box-shadow:0 4px 18px rgba(0,0,0,.1)}
.work-card .img{height:210px}
.work-card .name{position:absolute;left:20px;top:228px;font-size:13px;font-weight:700}
.work-card .tag{position:absolute;left:20px;top:256px;font-size:10px;border:1px solid var(--line);padding:2px 10px;color:var(--muted)}
.work-card .go{position:absolute;right:20px;top:232px;width:30px;height:30px;border-radius:50%;background:var(--red)}

/* column */
.col-title{left:160px;top:2030px;color:#fff;font-size:30px;font-weight:900}
.col-title small{display:block;font-size:11px;font-weight:500;margin-top:4px}
.col-btn{left:160px;top:2130px}
.col-illust{left:0;top:2250px;width:260px;height:220px;background:linear-gradient(180deg,#4f8bd6,#2f74cc);border-radius:0 120px 0 0}
.col-main{left:380px;top:2030px;width:320px;height:300px;background:#fff}
.col-main .img{height:190px}
.col-main .date,.col-sub .date{font-size:10px;color:var(--muted)}
.col-main .body{padding:14px 18px;font-size:12px;line-height:1.8;font-weight:500}
.col-sub{left:740px;width:300px;height:130px;background:#fff;display:flex}
.col-sub .img{width:130px;height:130px}
.col-sub .body{padding:12px 14px;font-size:12px;font-weight:700;line-height:1.7}

/* news */
.news-title{left:160px;top:2620px}
.news-btn{left:160px;top:2736px}
.news-list{left:400px;top:2630px;width:640px;list-style:none}
.news-list li{display:flex;align-items:center;height:66px;border-bottom:1px solid var(--line);font-size:12px;gap:30px;position:relative}
.news-list .date{font-family:"Montserrat",sans-serif;color:var(--muted);width:80px}
.news-list li::after{content:"";position:absolute;right:10px;width:6px;height:6px;border-radius:50%;background:var(--red)}

/* contents */
.contents-photo{left:0;top:3030px;width:600px;height:470px;border-radius:0 60px 0 0}
.contents-title{left:660px;top:3090px}
.contents-title small{display:block;font-size:11px;color:var(--muted);font-weight:500;margin-top:6px}
.contents-list{left:660px;top:3190px;width:380px;list-style:none}
.contents-list li{display:flex;align-items:center;gap:16px;height:80px;border-bottom:1px solid var(--line);font-size:14px;font-weight:700}
.contents-list .ico{width:36px;height:36px;border-radius:50%;background:var(--mist);display:flex;align-items:center;justify-content:center}
.contents-list .arr{margin-left:auto;width:6px;height:6px;border-radius:50%;background:var(--red)}

/* contact */
.contact{left:0;top:3560px;width:1200px;height:380px;background:var(--blue);color:#fff}
.contact-title{left:160px;top:3720px;font-size:30px;font-weight:900}
.contact-title small{display:block;font-size:11px;font-weight:500;margin-top:4px}
.contact-note{left:160px;top:3820px;font-size:11px;opacity:.85}
.contact-box{left:500px;top:3650px;width:540px}
.contact-box .company{font-size:11px;opacity:.85;padding-left:60px}
.contact-row{display:flex;align-items:center;gap:24px;height:100px;border-bottom:1px solid rgba(255,255,255,.4)}
.contact-row .num{font-family:"Montserrat",sans-serif;font-size:40px;font-weight:700}
.contact-row .mail{font-size:24px;font-weight:700}
.contact-row .arr{margin-left:auto;width:8px;height:8px;border-radius:50%;background:#fff}

/* footer */
.site-footer{left:0;top:3990px;width:1200px;height:694px;background:var(--mist)}
.f-brand{left:170px;top:4130px;display:flex;align-items:center;gap:10px}
.f-tel{left:170px;top:4220px;font-family:"Montserrat",sans-serif;color:var(--red);font-weight:700;font-size:20px}
.f-col{top:4110px;list-style:none;font-size:12px;line-height:2.4}
.f-col li.sub{padding-left:12px;color:var(--muted);font-size:11px}
.copy{left:0;top:4580px;width:1200px;text-align:center;font-size:10px;color:var(--muted)}
</style>
</head>
<body>

<header class="site-header">
  <div class="brand"><span class="brand-mark"></span><span class="brand-name">ファクトリーケア</span></div>
  <div class="util">
    <span>よくある質問</span><span>会社案内</span>
    <span class="tel">0256-71-3095</span>
    <span class="btn">カタログダウンロード</span>
    <span class="btn red">お問い合わせ</span>
  </div>
  <nav class="gnav">
    <span class="current">ホーム</span><span>ファクトリーケアの特徴</span><span>サービス一覧</span><span>施工事例</span><span>お問い合わせ</span>
  </nav>
</header>

<div class="abs hero photo" role="img" aria-label="ヘルメット姿の作業員が工場内で点検する写真"></div>
<div class="abs hero-copy">
  <p class="lead">工場専門の<em>技術</em>の高さで、</p>
  <p class="main">トラブルを解決。</p>
</div>

<section>
  <div class="abs intro-band"></div>
  <h2 class="abs intro-title">工場専門<br>修繕サービス</h2>
  <div class="abs intro-photo photo" role="img" aria-label="タブレットを持つ作業員の写真"></div>
  <p class="abs intro-text">工場や倉庫の修繕・改修・増築を専門に、現場の状況を丁寧に調査し最適な工事をご提案します。設備の老朽化や急なトラブルにも迅速に対応し、稼働を止めない施工計画をご用意します。小さな補修から大規模な改修まで、経験豊富なスタッフが責任を持って対応いたします。まずはお気軽にご相談ください。</p>
  <a class="abs intro-btn pill">詳しく見る</a>
  <div class="abs intro-photo2 photo" role="img" aria-label="倉庫内で作業する作業員の写真"></div>
  <div class="abs intro-bg-word">Factory Warehouse Repair</div>
</section>

<section>
  <h2 class="abs works-title sec-title">施工実績</h2>
  <a class="abs works-btn pill">施工実績一覧</a>
  <div class="abs works-band"></div>
  <article class="abs work-card" style="left:-180px"><div class="img photo" role="img" aria-label="工場内部の施工写真"></div><p class="name">株式会社〇〇〇</p><span class="tag">工場改修</span><span class="go"></span></article>
  <article class="abs work-card" style="left:160px"><div class="img photo" role="img" aria-label="工場内部の施工写真"></div><p class="name">株式会社〇〇〇</p><span class="tag">工場改修</span><span class="go"></span></article>
  <article class="abs work-card" style="left:500px"><div class="img photo" role="img" aria-label="工場内部の施工写真"></div><p class="name">株式会社〇〇〇</p><span class="tag">倉庫修繕</span><span class="go"></span></article>
  <article class="abs work-card" style="left:840px"><div class="img photo" role="img" aria-label="工場内部の施工写真"></div><p class="name">株式会社〇〇〇</p><span class="tag">増築工事</span><span class="go"></span></article>
  <article class="abs work-card" style="left:1180px"><div class="img photo" role="img" aria-label="工場内部の施工写真"></div><p class="name">株式会社〇〇〇</p><span class="tag">工場改修</span><span class="go"></span></article>
</section>

<section>
  <h2 class="abs col-title">コラム<small class="en">COLUMN</small></h2>
  <a class="abs col-btn pill white">コラム一覧</a>
  <div class="abs col-illust" role="img" aria-label="工具箱を運ぶ作業員のイラスト"></div>
  <article class="abs col-main">
    <div class="img photo" role="img" aria-label="工場で作業する人々の写真"></div>
    <div class="body"><p class="date">2024.01.20</p>工場の屋根修繕で押さえたい基本のポイントと費用の目安について解説</div>
  </article>
  <article class="abs col-sub" style="top:2030px">
    <div class="img photo" role="img" aria-label="作業員の写真"></div>
    <div class="body">倉庫の床補修を行う最適なタイミングとは<p class="date">2024.01.15</p></div>
  </article>
  <article class="abs col-sub" style="top:2180px">
    <div class="img photo" role="img" aria-label="作業員の写真"></div>
    <div class="body">設備移設の際に気をつけたい工事の流れ<p class="date">2024.01.10</p></div>
  </article>
</section>

<section>
  <h2 class="abs news-title sec-title">お知らせ</h2>
  <a class="abs news-btn pill">お知らせ一覧</a>
  <ul class="abs news-list">
    <li><span class="date">2024.01.20</span>年末年始の営業日についてのお知らせを掲載しました</li>
    <li><span class="date">2024.01.12</span>施工実績に工場改修工事の事例を追加しました</li>
    <li><span class="date">2024.01.05</span>カタログの最新版をダウンロード公開しました</li>
    <li><span class="date">2023.12.20</span>ホームページをリニューアルいたしました</li>
  </ul>
</section>

<section>
  <div class="abs contents-photo photo" role="img" aria-label="図面を確認する作業員の写真"></div>
  <h2 class="abs contents-title sec-title">コンテンツ<small class="en">CONTENTS</small></h2>
  <ul class="abs contents-list">
    <li><span class="ico"><svg width="18" height="18" viewBox="0 0 18 18"><circle cx="9" cy="9" r="7" fill="none" stroke="#1763c2" stroke-width="1.6"/><text x="9" y="13" text-anchor="middle" font-size="10" fill="#1763c2">?</text></svg></span>よくあるご質問<span class="arr"></span></li>
    <li><span class="ico"><svg width="18" height="18" viewBox="0 0 18 18"><rect x="3" y="3" width="12" height="12" fill="none" stroke="#1763c2" stroke-width="1.6"/></svg></span>会社のご案内<span class="arr"></span></li>
    <li><span class="ico"><svg width="18" height="18" viewBox="0 0 18 18"><path d="M9 3v9M5 8l4 4 4-4M3 15h12" fill="none" stroke="#1763c2" stroke-width="1.6"/></svg></span>カタログダウンロード<span class="arr"></span></li>
  </ul>
</section>

<section>
  <div class="abs contact"></div>
  <h2 class="abs contact-title" style="color:#fff">お問い合わせ<small class="en">CONTACT</small></h2>
  <p class="abs contact-note" style="color:#fff">ご相談やお見積りなど、お気軽にお問い合わせください。</p>
  <div class="abs contact-box" style="color:#fff">
    <p class="company">株式会社〇〇 工場修繕部門</p>
    <div class="contact-row">
      <svg width="34" height="34" viewBox="0 0 24 24"><path d="M6 3l3 0 2 5-2.5 1.5a11 11 0 0 0 6 6L16 13l5 2v3a2 2 0 0 1-2 2A17 17 0 0 1 4 5a2 2 0 0 1 2-2z" fill="none" stroke="#fff" stroke-width="1.6"/></svg>
      <span class="num">0256-71-3095</span>
    </div>
    <div class="contact-row">
      <svg width="34" height="34" viewBox="0 0 24 24"><rect x="3" y="5" width="18" height="14" fill="none" stroke="#fff" stroke-width="1.6"/><path d="M3 6l9 7 9-7" fill="none" stroke="#fff" stroke-width="1.6"/></svg>
      <span class="mail">無料お見積り・お問い合わせ</span><span class="arr"></span>
    </div>
  </div>
</section>

<footer>
  <div class="abs site-footer"></div>
  <div class="abs f-brand"><span class="brand-mark"></span><span class="brand-name">ファクトリーケア</span></div>
  <p class="abs f-tel">0256-71-3095</p>
  <ul class="abs f-col" style="left:540px"><li>ホーム</li><li>ファクトリーケアの特徴</li><li>施工事例</li><li>よくある質問</li><li>会社案内</li></ul>
  <ul class="abs f-col" style="left:720px"><li>サービス一覧</li><li class="sub">修繕工事</li><li class="sub">改修工事</li><li class="sub">増築工事</li><li class="sub">設備工事</li><li class="sub">その他のサービス</li></ul>
  <ul class="abs f-col" style="left:880px"><li>お知らせ</li><li>コラム</li><li>お問い合わせ</li><li>カタログダウンロード</li><li>プライバシーポリシー</li></ul>
  <p class="abs copy">Copyright © ファクトリーケア All Rights Reserved.</p>
</footer>

</body>
</html>
```